New corporate e-mail signature

We need a new e-mail signature for our company that is clean and professional. The requests are attached in a document.

Target Market(s)

CFO, CTO, Controllers, leaders, decision-makers.

Industry/Entity Type

Information Technology

Colors

Designer to choose colors to be used in the design.

Requirements
Must have
• See the PowerPoint document.
• - keep it as simple as possible.
• - same style as our new website design
• - It has to look good in all e-mail readers, and on all surfaces.
Nice to have
• - Please also attach 'best practise' for how to use the signature.
Should not have
• See the PowerPoint document. Use our color palette.
• - Do not include photo!

```html
<!DOCTYPE html>
<html lang="en">
<head>
<meta charset="utf-8">
<title>Valuecore – E-mail Signature</title>
<link rel="stylesheet" href="https://fonts.googleapis.com/css2?family=Open+Sans:wght@300;400;700&family=Mulish:wght@700&display=swap">
<style>
  :root {
    --page: #ffffff;
    --band-light: #5c9fcc;
    --band-mid: #2f6597;
    --band-dark: #1b3d6b;
    --band-edge: #9cc8e6;
    --ink-light: #ffffff;
    --accent: #3fc3c9;
    --caption: #111111;
  }
  * { box-sizing: border-box; margin: 0; padding: 0; }
  html, body { width: 1200px; height: 555px; overflow: hidden; background: var(--page); }
  body { position: relative; font-family: "Open Sans", Arial, sans-serif; color: var(--ink-light); }

  .signature {
    position: absolute; left: 0; width: 1178px; height: 190px;
    background:
      linear-gradient(180deg, rgba(255,255,255,0.35) 0, rgba(255,255,255,0) 6px),
      linear-gradient(172deg, rgba(255,255,255,0) 30%, rgba(255,255,255,0.12) 45%, rgba(255,255,255,0) 60%),
      linear-gradient(90deg, var(--band-light) 0%, var(--band-mid) 40%, var(--band-dark) 75%, var(--band-dark) 100%);
    border-top: 2px solid var(--band-edge);
  }
  .signature::after {
    content: ""; position: absolute; left: 0; right: 0; bottom: 12px; height: 3px;
    background: linear-gradient(90deg, rgba(255,255,255,0.5), rgba(255,255,255,0.15));
  }
  .signature--logo { top: 10px; }
  .signature--plain { top: 222px; }

  .identity { position: absolute; top: 56px; text-align: center; }
  .identity__name { font-weight: 300; font-size: 34px; line-height: 1.1; }
  .identity__role { font-weight: 700; font-size: 24px; line-height: 1.3; }

  .contact { position: absolute; top: 42px; list-style: none; }
  .contact__row { display: flex; align-items: baseline; height: 37px; font-size: 22px; }
  .contact__label { width: 30px; font-size: 14px; color: var(--accent); font-weight: 700; }

  .divider { position: absolute; top: 70px; width: 14px; height: 54px; }

  .social { position: absolute; top: 76px; display: flex; gap: 16px; }
  .social__tile { width: 45px; height: 45px; border-radius: 7px; background: var(--ink-light); }

  .brand { position: absolute; top: 78px; left: 1000px; font-weight: 700; font-size: 28px; color: var(--ink-light); }

  .signature--logo .identity { left: 55px; width: 240px; }
  .signature--logo .contact { left: 375px; }
  .signature--logo .divider { left: 678px; }
  .signature--logo .social { left: 735px; }
  .signature--plain .identity { left: 118px; width: 240px; }
  .signature--plain .contact { left: 450px; }
  .signature--plain .divider { left: 752px; }
  .signature--plain .social { left: 810px; }

  .caption { position: absolute; font-family: "Mulish", Arial, sans-serif; font-weight: 700; color: var(--caption); }
  .caption--version { left: 12px; top: 498px; font-size: 15px; }
  .caption--brief { left: 645px; top: 448px; font-size: 15px; line-height: 24px; list-style: none; }
</style>
</head>
<body>

<section class="signature signature--logo">
  <div class="identity">
    <p class="identity__name">Erik Lund</p>
    <p class="identity__role">Senior Manager</p>
  </div>
  <ul class="contact">
    <li class="contact__row"><span class="contact__label">T•</span>+47 900 12 345</li>
    <li class="contact__row"><span class="contact__label">E•</span>post@valuecore.no</li>
    <li class="contact__row"><span class="contact__label">W•</span>www.valuecore.com</li>
  </ul>
  <svg class="divider" viewBox="0 0 14 54" aria-hidden="true">
    <rect x="0" y="0" width="14" height="5" fill="var(--accent)"/>
    <rect x="0" y="24" width="14" height="5" fill="var(--accent)"/>
    <rect x="0" y="48" width="14" height="5" fill="var(--accent)"/>
  </svg>
  <div class="social" role="img" aria-label="Social network links">
    <span class="social__tile"></span><span class="social__tile"></span><span class="social__tile"></span>
  </div>
  <p class="brand">valuecore</p>
</section>

<section class="signature signature--plain">
  <div class="identity">
    <p class="identity__name">Erik Lund</p>
    <p class="identity__role">Senior Manager</p>
  </div>
  <ul class="contact">
    <li class="contact__row"><span class="contact__label">T•</span>+47 900 12 345</li>
    <li class="contact__row"><span class="contact__label">E•</span>post@valuecore.no</li>
    <li class="contact__row"><span class="contact__label">W•</span>www.valuecore.com</li>
  </ul>
  <svg class="divider" viewBox="0 0 14 54" aria-hidden="true">
    <rect x="0" y="0" width="14" height="5" fill="var(--accent)"/>
    <rect x="0" y="24" width="14" height="5" fill="var(--accent)"/>
    <rect x="0" y="48" width="14" height="5" fill="var(--accent)"/>
  </svg>
  <div class="social" role="img" aria-label="Social network links">
    <span class="social__tile"></span><span class="social__tile"></span><span class="social__tile"></span>
  </div>
</section>

<p class="caption caption--version">Logo &amp; non-logo version - 02</p>
<ul class="caption caption--brief">
  <li>-Client: Symbol - Valuecore</li>
  <li>-Request: E-Signature</li>
  <li>-Product: Corporative e-mail signature</li>
  <li>-Characteristics: Information Technology, decision makers, leaders.</li>
</ul>

</body>
</html>
```